Book Cover Design Project

I have written a booK called "Build From Nothing:
a handbook for launching and steering a modest enterprise. It is aimed at the start up entrepreneur and seeks to give them everything they need to start up and run a small business. I am interested in a very simple cover that is contemporary in the look but clearly communicates the mission of the book. It should sell very well as there are no others like it, so the designer will get excellent exposure.
Updates

Reason: I an vacation in Europe until the 23rd of July. Would like a few days to make a decision after my return Ned

We are currently on vacation.  Will make a final decision in about a week.  Thanks so much for your submissions

Ned

Target Market(s)

Start up businesses in the U.S.

Industry/Entity Type

Business

Requirements
Must have
• Clear communication of the name. Lots of white space. Graphic communication of the purpose of the book? Prominent exposure of my name. Edward r. Kistlewood

```html
<!DOCTYPE html>
<html lang="en">
<head>
<meta charset="utf-8">
<title>Build From Nothing – Book Cover</title>
<link rel="stylesheet" href="https://fonts.googleapis.com/css2?family=Bebas+Neue&display=swap">
<style>
  :root {
    --backdrop: #161616;
    --paper: #ffffff;
    --ink: #000000;
    --band: #7b2c0c;
    --band-text: #ffffff;
    --coin-light: #f1c58a;
    --coin-mid: #c98a3c;
    --coin-dark: #8a5420;
  }
  * { margin: 0; padding: 0; box-sizing: border-box; }
  html, body {
    width: 1200px;
    height: 900px;
    overflow: hidden;
    background: var(--backdrop);
  }
  .stage {
    width: 1200px;
    height: 900px;
    display: flex;
    align-items: center;
    justify-content: center;
  }
  .book-cover {
    width: 464px;
    height: 720px;
    background: var(--paper);
    display: flex;
    flex-direction: column;
    align-items: center;
    font-family: "Bebas Neue", "Arial Narrow", sans-serif;
    color: var(--ink);
  }
  .author-band {
    width: 100%;
    height: 30px;
    background: var(--band);
    color: var(--band-text);
    font-size: 24px;
    letter-spacing: 4px;
    line-height: 31px;
    text-align: center;
  }
  .book-title {
    margin-top: 22px;
    font-size: 124px;
    line-height: 0.98;
    font-weight: 400;
    text-align: center;
    letter-spacing: 1px;
  }
  .book-title span { display: block; }
  .cover-illustration {
    margin-top: 28px;
    width: 320px;
    height: 150px;
    background:
      radial-gradient(ellipse 60% 75% at 50% 100%, var(--coin-mid) 0%, var(--coin-light) 45%, rgba(255,255,255,0) 72%);
    border-bottom: 4px solid var(--coin-dark);
    border-radius: 2px;
  }
  .book-subtitle {
    margin-top: 30px;
    font-size: 48px;
    line-height: 1.12;
    font-weight: 400;
    text-align: center;
  }
  .book-subtitle span { display: block; }
</style>
</head>
<body>
  <main class="stage">
    <article class="book-cover">
      <header class="author-band">Author Name</header>
      <h1 class="book-title">
        <span>Build From</span>
        <span>Nothing:</span>
      </h1>
      <div class="cover-illustration" role="img" aria-label="Businessman in a suit climbing rising stacks of gold coins"></div>
      <h2 class="book-subtitle">
        <span>A Handbook For</span>
        <span>Launching &amp; Steering</span>
        <span>A Modest Enterprise</span>
      </h2>
    </article>
  </main>
</body>
</html>
```